Social Media Application Design - Android and IOS

I am ready to go live with new social media app however I am not comfortable with the current design. It is a not interactive or attractive enough. Please note the splash screen is a green, so preference would be to keep a green theme although I am more than happy to consider other colours that would improve the design.
The attachment has the app screens that need to be redesigned. They may not need massive changes , however keen to go live so looking for inspired designers to support with this project and many others that I have, including ongoing work on this app.
Target Market(s)
Millenials
Industry/Entity Type
Social
Colors
Designer to choose colors to be used in the design.
Requirements
Must have
- Please see attached document for screens that I would like redesigned. It needs to work with Android and IOS. I am looking for the design and not the functionality.
Nice to have
- Highly interactive design. Please see polling functionality of Loomrix.
Should not have
- should not be complicated - simplicity is the key

```html
<!DOCTYPE html>
<html lang="en">
<head>
<meta charset="utf-8">
<title>Side Menu</title>
<link rel="stylesheet" href="https://fonts.googleapis.com/css2?family=Ubuntu:wght@400;500;700&display=swap">
<style>
  :root {
    --bg-top: #a14ad5;
    --bg-bottom: #8a4ad6;
    --strip-top: #7c4ad4;
    --strip-bottom: #9b4ad5;
    --hill: #9d4bd5;
    --ring: rgba(255, 255, 255, 0.14);
    --photo: #c9b7a8;
    --photo-dark: #8f7766;
    --text: #ffffff;
    --toggle-track: #7d45cf;
    --button: #7f45cc;
    --highlight: rgba(120, 50, 190, 0.35);
  }
  * { margin: 0; padding: 0; box-sizing: border-box; }
  html, body { width: 675px; height: 1200px; overflow: hidden; }
  body {
    font-family: "Ubuntu", sans-serif;
    color: var(--text);
    background: linear-gradient(180deg, var(--bg-top) 0%, var(--bg-bottom) 75%);
    position: relative;
  }
  .side-strip {
    position: absolute; left: 562px; top: 0; width: 113px; height: 100%;
    background: linear-gradient(180deg, var(--strip-top) 0%, var(--strip-bottom) 80%);
  }
  .hill { position: absolute; left: 0; top: 0; }
  .profile { position: absolute; left: 0; top: 0; width: 100%; }
  .avatar-ring {
    position: absolute; left: 42px; top: 58px; width: 198px; height: 198px;
    border-radius: 50%; background: var(--ring);
  }
  .avatar-photo {
    position: absolute; left: 15px; top: 15px; width: 168px; height: 168px;
    border-radius: 50%;
    background: radial-gradient(circle at 50% 40%, var(--photo) 0%, var(--photo-dark) 100%);
  }
  .user-name {
    position: absolute; left: 272px; top: 106px;
    font-size: 26px; font-weight: 700; letter-spacing: 0.5px;
  }
  .user-email {
    position: absolute; left: 273px; top: 148px; font-size: 15px;
  }
  .notify-row {
    position: absolute; left: 273px; top: 192px; display: flex; align-items: center;
  }
  .notify-label { font-size: 15.5px; }
  .toggle {
    margin-left: 13px; width: 64px; height: 25px; position: relative;
    background: var(--toggle-track); border-radius: 3px;
  }
  .toggle-state {
    position: absolute; left: 7px; top: 6px; font-size: 10px; opacity: 0.85;
  }
  .toggle-knob {
    position: absolute; right: 0; top: 0; width: 36px; height: 25px;
    background: #fff; border-radius: 4px; box-shadow: 0 3px 6px rgba(60, 20, 110, 0.35);
  }
  .menu { position: absolute; left: 0; top: 367px; width: 100%; list-style: none; }
  .menu-item {
    height: 85px; line-height: 64px; padding-left: 96px; font-size: 23.5px;
  }
  .menu-item.is-active {
    margin-left: 40px; padding-left: 56px; width: 316px; height: 64px; margin-bottom: 21px;
    background: linear-gradient(90deg, var(--highlight) 0%, rgba(120, 50, 190, 0.2) 70%, rgba(120, 50, 190, 0) 100%);
  }
  .footer-button {
    position: absolute; top: 1123px; height: 77px; background: var(--button);
    display: flex; align-items: center; justify-content: center; gap: 12px;
    font-size: 24px;
  }
  .footer-button.settings { left: 0; width: 325px; }
  .footer-button.logout { left: 349px; width: 326px; padding-top: 6px; }
</style>
</head>
<body>
  <div class="side-strip"></div>
  <svg class="hill" width="675" height="1200" viewBox="0 0 675 1200" aria-hidden="true">
    <circle cx="333" cy="1175" r="360" fill="var(--hill)"/>
    <rect x="0" y="1080" width="675" height="120" fill="var(--hill)"/>
  </svg>

  <header class="profile">
    <div class="avatar-ring">
      <div class="avatar-photo" role="img" aria-label="Profile photo of the user"></div>
    </div>
    <h1 class="user-name">MARCUS VALE</h1>
    <p class="user-email">marcus@pawmail.com</p>
    <div class="notify-row">
      <span class="notify-label">Allow Notifications</span>
      <span class="toggle"><span class="toggle-state">ON</span><span class="toggle-knob"></span></span>
    </div>
  </header>

  <ul class="menu">
    <li class="menu-item is-active">Home</li>
    <li class="menu-item">My Profile</li>
    <li class="menu-item">My Activities</li>
    <li class="menu-item">Notifications</li>
    <li class="menu-item">Contact us</li>
  </ul>

  <div class="footer-button settings">
    <svg width="22" height="22" viewBox="0 0 24 24" fill="none" stroke="#fff" stroke-width="1.3" aria-hidden="true">
      <circle cx="12" cy="12" r="3.2"/>
      <path d="M10.3 2h3.4l.5 2.6 1.9.8 2.2-1.5 2.4 2.4-1.5 2.2.8 1.9 2.6.5v3.4l-2.6.5-.8 1.9 1.5 2.2-2.4 2.4-2.2-1.5-1.9.8-.5 2.6h-3.4l-.5-2.6-1.9-.8-2.2 1.5-2.4-2.4 1.5-2.2-.8-1.9L2 13.7v-3.4l2.6-.5.8-1.9-1.5-2.2 2.4-2.4 2.2 1.5 1.9-.8z"/>
    </svg>
    <span>Setting</span>
  </div>
  <div class="footer-button logout">
    <svg width="26" height="26" viewBox="0 0 26 26" fill="none" stroke="#fff" stroke-width="1.6" aria-hidden="true">
      <path d="M6 7.5A9.5 9.5 0 1 1 6 18.5"/>
      <path d="M2 13h13M6 9l-4 4 4 4"/>
    </svg>
    <span>Log out</span>
  </div>
</body>
</html>
```